Maple Ridge business card design

Card needs to include the following text/items:
Company Logo
Tobin Marsh
Phone # - 555-318-7642
service@mapleridgelandscaping.example
Lawn & landscape maintenance services

```html
<!DOCTYPE html>
<html lang="en">
<head>
<meta charset="utf-8">
<title>Maple Ridge Business Card</title>
<link href="https://fonts.googleapis.com/css2?family=Cinzel:wght@600;700&family=Montserrat:wght@400;500&display=swap" rel="stylesheet">
<style>
  :root {
    --canvas: #8a6b45;
    --card: #1c1c1c;
    --card-sheen: #2c2c2c;
    --white: #ffffff;
    --gold: #e0a81c;
    --green: #8fb33a;
    --soft: #d9d9d9;
  }
  * { box-sizing: border-box; margin: 0; padding: 0; }
  html, body { width: 1200px; height: 900px; overflow: hidden; }
  body {
    background: var(--canvas);
    display: flex;
    flex-direction: column;
    align-items: center;
    justify-content: center;
    gap: 40px;
  }
  .card {
    width: 660px;
    height: 380px;
    border-radius: 22px;
    background: linear-gradient(135deg, var(--card) 0%, var(--card-sheen) 45%, var(--card) 100%);
    box-shadow: 0 14px 30px rgba(0,0,0,.35);
    position: relative;
    color: var(--white);
  }
  .brand {
    display: flex;
    align-items: center;
    gap: 14px;
  }
  .brand-dot {
    width: 34px; height: 34px; border-radius: 50%;
    background: var(--green);
  }
  .brand-name {
    font-family: "Cinzel", serif;
    font-weight: 700;
    font-size: 38px;
    color: var(--white);
    letter-spacing: 1px;
  }
  /* front */
  .card-front {
    display: flex;
    flex-direction: column;
    align-items: center;
    justify-content: center;
    gap: 44px;
  }
  .tagline {
    font-family: "Cinzel", serif;
    font-weight: 600;
    font-size: 19px;
    letter-spacing: 4px;
    text-align: center;
    line-height: 1.5;
    text-transform: uppercase;
  }
  /* back */
  .card-back {
    display: flex;
    align-items: center;
    padding: 0 50px 0 70px;
  }
  .card-back .brand-name { font-size: 30px; }
  .card-back .brand-dot { width: 28px; height: 28px; }
  .divider {
    width: 2px; height: 150px;
    background: var(--gold);
    margin: 0 36px 0 40px;
  }
  .contact { font-family: "Montserrat", sans-serif; }
  .person-name {
    font-family: "Cinzel", serif;
    font-weight: 700;
    font-size: 24px;
    margin-bottom: 2px;
  }
  .person-name .first { color: var(--green); }
  .person-name .last { color: var(--gold); }
  .role { font-size: 15px; color: var(--soft); margin-bottom: 18px; }
  .line {
    display: flex; align-items: center; gap: 9px;
    font-size: 14px; color: var(--white); margin-top: 6px;
  }
  .line svg { width: 14px; height: 14px; flex: none; }
</style>
</head>
<body>
  <section class="card card-front">
    <div class="brand">
      <span class="brand-dot"></span>
      <span class="brand-name">Maple Ridge</span>
    </div>
    <p class="tagline">Lawn &amp; Landscape<br>Maintenance Services</p>
  </section>

  <section class="card card-back">
    <div class="brand">
      <span class="brand-dot"></span>
      <span class="brand-name">Maple Ridge</span>
    </div>
    <span class="divider"></span>
    <div class="contact">
      <h1 class="person-name"><span class="first">Tobin</span> <span class="last">Marsh</span></h1>
      <p class="role">Managing Director</p>
      <p class="line">
        <svg viewBox="0 0 24 24" fill="var(--gold)" aria-hidden="true"><path d="M6.6 10.8a15.1 15.1 0 0 0 6.6 6.6l2.2-2.2c.3-.3.7-.4 1-.2 1.1.4 2.3.6 3.6.6.6 0 1 .4 1 1V20c0 .6-.4 1-1 1A17 17 0 0 1 3 4c0-.6.4-1 1-1h3.5c.6 0 1 .4 1 1 0 1.3.2 2.5.6 3.6.1.3 0 .7-.2 1z"/></svg>
        555-318-7642
      </p>
      <p class="line">
        <svg viewBox="0 0 24 24" fill="none" stroke="var(--gold)" stroke-width="2.2" aria-hidden="true"><rect x="3" y="5" width="18" height="14" rx="1.5"/><path d="M3 6l9 7 9-7"/></svg>
        service@mapleridgelandscaping.example
      </p>
    </div>
  </section>
</body>
</html>
```